New Australian Event targeting the Office Industry Web Design Project

Deskora* is an exhibition and conference aimed at meeting the business needs of office professionals – the visitors are the ones that make purchase decisions when buying anything to do with the office from office equipment and stationery, event management, training and travel.

The range of exhibitors at this show is unique in Aust – therefore no other show that is similar or as relevant for this target market.
Being that it is a new show – visitors and exhibitors will want a better understanding of what the show is about, and how it is beneficial to them.

Deskora UK, Canada & US – will need to keep similar ‘brand guidelines’ but the functionality and layout is not appropriate. Eg. half a page on static banner branding is waste of space.
http://www.deskorafair.co.uk/ and www.deskoranorth.ca and http://www.deskora-expohall.com/

Some examples of Aus websites who are targeting same type of customer:
http://www.workwrenfolk.com.au/
http://www.tolvane.com.au/
http://www.quillanwares.com.au/quillan/en_au/

Hi All, 

Thanks for the interest in our competition, I will be away until the 11th of January at which point i will comment on the designs. 

Thanks and Merry Xmas. 

Target Market(s)

Office Managers, Executive Assistants / Personal Assistants, Office Professionals,

Industry/Entity Type

Training

Requirements
Must have
• The website will be built into a CMS. The website will need to offer:

Homepage:
Clear CTA's - Visitor (Register free) and Exhibitor (Book a Stand)
“what’s new/hot” section on homepage
3 or 4 content areas for in-event promotions
Data capture – this will need to very visible on home page
All to fit within 'one fold'.

Content Page:
Relevant CTA's - Visitor (Register free) and Exhibitor (Book a Stand)

Sitewide:
Social media integration

I would like to see designs for a content page as well as the homepage.
Nice to have
• Floating navigation/call to action bar (top, bottom or side) - eg, http://brisklinewire.com/me/2011/12/20/hacker-group-disrupts-state-portals-in-region-again/, http://ponderly.com/2011/12/19/snapvale-2011/
Should not have
• Elements requiring Flash

```html
<!DOCTYPE html>
<html lang="en">
<head>
<meta charset="utf-8">
<title>Deskora 2012 – Home</title>
<link href="https://fonts.googleapis.com/css2?family=Jost:wght@400;500;600&display=swap" rel="stylesheet">
<style>
:root{
  --ink:#2b2728;
  --header:#231f20;
  --pink:#d6127f;
  --pink-soft:#fbe3f0;
  --blue:#2aaef0;
  --blue-light:#7fd3fb;
  --panel:#ececec;
  --line:#c9c9c9;
  --text:#4a4a4a;
  --white:#ffffff;
}
*{box-sizing:border-box;margin:0;padding:0}
html,body{width:901px;height:1200px;overflow:hidden}
body{font-family:"Jost",sans-serif;color:var(--text);position:relative;
  background:linear-gradient(180deg,var(--header) 0,var(--header) 174px,var(--pink) 174px,var(--pink) 179px,var(--pink-soft) 179px,#fff 520px,#fff 100%);}
.page{position:absolute;left:40px;top:44px;width:822px;height:1062px;background:var(--white);
  border:2px solid var(--line);border-radius:8px;overflow:hidden;box-shadow:0 1px 4px rgba(0,0,0,.25)}
.masthead{position:absolute;left:0;top:0;width:100%;height:134px;background:var(--header)}
.brand{position:absolute;left:40px;top:34px;color:var(--white)}
.brand-name{font-size:46px;font-weight:500;line-height:1;letter-spacing:-1px}
.brand-date{font-size:10px;margin-top:8px;color:var(--white)}
.contact{position:absolute;right:30px;top:27px;display:flex;gap:14px;color:var(--white);font-size:16px;line-height:32px}
.contact-icon{width:32px;height:32px;background:var(--pink);border-radius:4px;display:flex;align-items:center;justify-content:center;margin-top:8px}
.nav{position:absolute;left:4px;top:136px;width:812px;height:46px;display:flex;align-items:center;
  background:linear-gradient(#fafafa,#d8d8d8)}
.nav a{font-size:13px;color:#333;text-decoration:none;padding:0 12px;height:46px;line-height:46px;border-right:1px solid #bdbdbd}
.nav a.current{background:var(--pink);color:#fff;border-radius:4px 4px 0 0;height:32px;line-height:32px;margin:10px 4px 0 20px;padding:0 13px;border:0;border-radius:4px}
.register{position:absolute;left:8px;top:189px;width:220px;height:274px;border-radius:8px;border:1px solid #1b8fd0;
  background:linear-gradient(var(--blue-light),var(--blue) 40%,#3fb9f3);padding:12px 0 0}
.register h2{font-size:19px;font-weight:400;color:#222;line-height:26px;margin-left:56px}
.register .badge{position:absolute;left:12px;top:20px;width:30px;height:30px;background:#f4c21c;border-radius:4px}
.roles{display:flex;gap:22px;margin:10px 0 0 24px;font-size:15px;color:#222}
.roles span::before{content:"";display:inline-block;width:12px;height:12px;border-radius:50%;background:#fff;border:1px solid #555;margin-right:6px;vertical-align:-1px}
.roles .on::before{background:radial-gradient(#333 3px,#fff 4px)}
.field{display:block;width:160px;height:24px;border-radius:4px;background:#fff;border:1px solid #9ccbe6;font-size:10px;color:#333;padding-left:16px;line-height:22px;margin:0 0 12px 28px}
.register .field:first-of-type{margin-top:24px}
.btn-dark{display:block;margin:8px 0 0 68px;width:116px;height:34px;border-radius:4px;background:linear-gradient(#555,#111);color:#fff;font-size:13px;text-align:center;line-height:34px}
.hero{position:absolute;left:238px;top:189px;width:574px;height:272px;border-radius:6px;overflow:hidden;
  background:linear-gradient(135deg,#5b5a55,#a39a8c 45%,#3b3a37)}
.hero-caption{position:absolute;left:0;right:0;top:182px;text-align:center;color:#fff;text-shadow:0 1px 3px #000}
.hero-caption .a{font-size:16px;line-height:24px}.hero-caption .b{font-size:20px;line-height:28px}.hero-caption .c{font-size:16px;line-height:26px}
.starburst{position:absolute;right:12px;top:14px}
.dots{position:absolute;right:18px;bottom:12px;display:flex;gap:6px}
.dots i{width:14px;height:14px;border-radius:50%;background:#f6d8e9}.dots i:first-child{background:var(--pink)}
.side-card{position:absolute;left:8px;width:220px;border:1px solid var(--line);border-radius:8px;background:linear-gradient(#fff,var(--panel))}
.whats-new{top:478px;height:180px}
.card-title{margin:6px;height:32px;border-radius:4px;background:var(--pink);color:#fff;font-size:16px;line-height:32px;text-align:center}
.news-photo{position:absolute;left:6px;top:52px;width:90px;height:88px;background:linear-gradient(#6d6b78,#b98778)}
.news-text{position:absolute;left:108px;top:52px;width:104px;font-size:9.5px;color:#333;line-height:12.5px}
.news-text p{margin-bottom:12px}
.more{position:absolute;left:110px;top:156px;font-size:9px;color:var(--pink)}
.video{position:absolute;left:8px;top:666px;width:220px;height:152px;border-radius:8px;overflow:hidden;background:var(--header);border:1px solid #666}
.video-name{position:absolute;left:0;right:0;top:44px;text-align:center;color:#fff;font-size:30px;font-weight:500}
.video-bar{position:absolute;left:0;bottom:0;width:100%;height:10px;background:linear-gradient(#ddd,#999)}
.query{top:830px;height:206px}
.query h3{font-size:17px;font-weight:400;color:#222;margin:8px 0 13px 20px;line-height:25px}
.query .field{margin:0 0 8px 18px;width:160px;font-size:9px;color:#777;border-color:#999}
.query .message{height:54px;line-height:30px}
.btn-pink{display:block;margin:5px 0 0 66px;width:64px;height:28px;border-radius:4px;background:var(--pink);color:#fff;font-size:11px;text-align:center;line-height:28px}
.welcome{position:absolute;left:262px;top:482px;width:550px}
.welcome h1{font-size:18px;font-weight:400;color:#222}
.welcome h1 span{color:var(--pink);font-size:20px}
.welcome-body{margin-top:10px;margin-left:4px;width:500px;font-size:11.8px;line-height:15px;color:#444}
.welcome-body p{margin-bottom:15px}
.welcome-body p.lead{width:456px}
.welcome-body a{color:var(--pink);text-decoration:none}
.portrait{position:absolute;right:-30px;top:36px;width:70px;height:94px;border:1px solid #777;background:linear-gradient(#e6e6e6,#8c8c8c)}
.rule{position:absolute;left:266px;top:810px;width:540px;border-top:1px dotted #999}
.events h2{position:absolute;left:268px;top:830px;font-size:16px;font-weight:400;color:#222}
.arrow{position:absolute;top:926px;width:18px;height:18px;border-radius:50%;background:#222}
.thumb{position:absolute;top:876px;width:134px;height:124px;border-radius:4px;border:1px solid #aaa}
.footer-social{position:absolute;left:54px;top:1131px;display:flex;gap:4px}
.footer-social i{width:28px;height:28px;border-radius:5px}
.footer-links{position:absolute;right:52px;top:1129px;font-size:10px;color:#222}
.footer-links span{margin:0 6px;color:#666}
.copyright{position:absolute;left:502px;top:1162px;font-size:10.5px;color:#222}
</style>
</head>
<body>
<div class="page">
  <header class="masthead">
    <div class="brand">
      <div class="brand-name">Deskora</div>
      <div class="brand-date">12-13 September 2012 Halvern Hall | London</div>
    </div>
    <div class="contact">
      <div class="contact-icon">
        <svg width="18" height="20" viewBox="0 0 18 20"><path d="M4 1l3 4-2 2c1 3 3 5 6 7l2-2 4 3-2 3C8 18 1 11 1 3z" fill="#231f20"/></svg>
      </div>
      <div>01632 960132<br>01632 960115</div>
    </div>
  </header>
  <nav class="nav">
    <a class="current">Home</a><a>011 Show Review</a><a>National PA Day 2011</a><a>Exhibitor</a><a>Visitor</a><a>Press</a><a>Venue</a><a>Travel &amp; Hotels</a><a style="border:0">Charity Partner</a>
  </nav>

  <section class="register">
    <i class="badge"></i>
    <h2>Register free &amp;<br>Book a Stand</h2>
    <div class="roles"><span class="on">Visitor</span><span>Exhibitor</span></div>
    <span class="field">Name</span>
    <span class="field">Email</span>
    <span class="btn-dark">Register Now</span>
  </section>

  <section class="hero" role="img" aria-label="Photo of two office professionals talking at a desk">
    <svg class="starburst" width="104" height="90" viewBox="0 0 104 90">
      <polygon fill="#d6127f" points="52,0 60,12 74,5 76,20 92,17 88,32 104,36 93,46 104,56 88,60 92,74 76,71 74,86 60,79 52,90 44,79 30,86 28,71 12,74 16,60 0,56 11,46 0,36 16,32 12,17 28,20 30,5 44,12"/>
      <text x="52" y="35" text-anchor="middle" fill="#fff" font-family="Jost,sans-serif" font-size="11">NEWS</text>
      <text x="52" y="50" text-anchor="middle" fill="#fff" font-family="Jost,sans-serif" font-size="11">VENUE FOR</text>
      <text x="52" y="65" text-anchor="middle" fill="#fff" font-family="Jost,sans-serif" font-size="11">2012!</text>
    </svg>
    <div class="hero-caption">
      <div class="a">Your ultimate event to meet and do business with</div>
      <div class="b">PAs, EAs &amp; Office Managers</div>
      <div class="c">12-13 September 2012 Halvern Hall &nbsp;| &nbsp;London</div>
    </div>
    <div class="dots"><i></i><i></i><i></i><i></i></div>
  </section>

  <section class="side-card whats-new">
    <div class="card-title">What’s New Module</div>
    <div class="news-photo" role="img" aria-label="Photo of visitors at the show"></div>
    <div class="news-text">
      <p>Lorem ipsum dolor sit amet, consectetuer adipiscing elit.</p>
      <p>Lorem ipsum dolor sit amet, consectetuer adipiscing elit.</p>
    </div>
    <span class="more">View More &gt;&gt;</span>
  </section>

  <section class="video" aria-label="Show video player">
    <div class="video-name">Deskora</div>
    <svg style="position:absolute;left:96px;top:58px" width="26" height="26" viewBox="0 0 26 26"><circle cx="13" cy="13" r="13" fill="rgba(255,255,255,.3)"/><path d="M10 7l9 6-9 6z" fill="#fff"/></svg>
    <div class="video-bar"></div>
  </section>

  <section class="side-card query">
    <h3>Query</h3>
    <span class="field">Name</span>
    <span class="field">Email</span>
    <span class="field message">Message</span>
    <span class="btn-pink">Submit</span>
  </section>

  <section class="welcome">
    <h1>Welcome to <span>Deskora</span></h1>
    <div class="portrait" role="img" aria-label="Portrait of the show director"></div>
    <div class="welcome-body">
      <p class="lead">The essential event for career focused PAs, EAs &amp; Office Managers. Fresh from the success of our second fantastic show which saw the launch of National PA Day, the first ever online portal for Office Managers, DESKNET.co.uk as well as many other new and innovative products and services all aimed at enabling todays office professional to excel in their increasingly demanding job roles.</p>
      <p>Deskora 2011 saw visitor numbers increase by 18% and exhibitors by 26% – the feedback so far is brilliant from both sides with an incredible 60% of exhibitors rebooking onsite!</p>
      <p>Please browse this website to see what was on offer this year as we update the site ready for an even bigger and better show for 2012 – having already outgrown our venue we move to Grand Hall, Halvern next year so keep an eye out for the latest developments as they happen.</p>
      <p><a>Read more…</a></p>
      <p>Mark your diary for Wednesday 12th and Thursday 13th of September 2012!</p>
      <p>1st annual National PA Survey results announced - UK Survey reveals feelings of the nation’s PAs</p>
    </div>
  </section>

  <div class="rule"></div>
  <section class="events">
    <h2>Latest Events</h2>
    <span class="arrow" style="left:282px"><svg width="18" height="18"><path d="M10 6l-3 3 3 3" stroke="#fff" stroke-width="1.6" fill="none"/></svg></span>
    <div class="thumb" style="left:312px;background:linear-gradient(#7a6d6a,#d9a3b8)" role="img" aria-label="Photo of the exhibition floor"></div>
    <div class="thumb" style="left:462px;background:linear-gradient(#2a2a2a,#8b7a66)" role="img" aria-label="Photo of a speaker at the show"></div>
    <div class="thumb" style="left:612px;background:linear-gradient(#5a4a55,#c0708e)" role="img" aria-label="Photo of crowds in the exhibition hall"></div>
    <span class="arrow" style="left:758px"><svg width="18" height="18"><path d="M8 6l3 3-3 3" stroke="#fff" stroke-width="1.6" fill="none"/></svg></span>
  </section>
</div>

<div class="footer-social" aria-label="Social links">
  <i style="background:#2d5aa8"></i><i style="background:#3fa9e0"></i><i style="background:#1c6aa8"></i><i style="background:#f08a24"></i>
</div>
<div class="footer-links">Brightwell Trade Events UK<span>|</span>Supporters Page<span>|</span>Terms and Conditions<span>|</span>Privacy Policy<span>|</span>Contact Us</div>
<div class="copyright">Copyright © Deskora, All Rights Reserved</div>
</body>
</html>
```